High-end Investment firm website

It needs to feel very high-end. We like clean design which incorporates a good deal of white space with the use of imagery to be provided.

Here are a few examples of design which is appealing:
https://www.brindlecrestcapital.example
https://www.larkmoorgroup.example

Please use the following shade of blue in the design #7BAFD4.

Additional brand colors black, grey and white.

This quorvex doc has a link to all of the content for the site. It also has detailed design notes per section.

https://files.quorvexdocs.example/document/d/7TRQ2WpeLmnb8cvdKa3HJ0XsNf5ZgR1YtUoC9eV4qAs/edit?usp=sharing

Target Market(s)

Investors and companies in our target industries

Industry/Entity Type

Investment

Coding

Coded - Design and coding required

Number of Pages Required

5+ page

Font styles to use
Sans Serif

Requirements
Must have
• Clean feel, lots of white space.
Nice to have
• Clean graphics similar to https://www.brindlecrestcapital.example

```html
<!DOCTYPE html>
<html lang="en">
<head>
<meta charset="utf-8">
<title>Corvane Industries</title>
<link rel="stylesheet" href="https://fonts.googleapis.com/css2?family=Montserrat:wght@400;500;600&family=Open+Sans:wght@400;600&display=swap">
<style>
:root{
  --brand:#7BAFD4;
  --brand-dark:#5e95be;
  --ink:#222428;
  --text:#6d6f74;
  --muted:#9a9ca1;
  --line:#e3e5e8;
  --paper:#ffffff;
  --soft:#f7f8fa;
  --footer:#1f2024;
}
*{box-sizing:border-box;margin:0;padding:0}
html,body{width:1200px;height:4108px;overflow:hidden}
body{position:relative;background:var(--paper);font-family:"Open Sans",sans-serif;color:var(--text)}
.abs{position:absolute}
.photo{position:absolute}
.btn{position:absolute;background:var(--brand);color:#fff;font:600 11px "Open Sans",sans-serif;letter-spacing:.5px;display:flex;align-items:center;justify-content:center;text-transform:uppercase}

.topbar{left:0;top:0;width:1200px;height:33px;background:var(--brand)}
.topbar p{position:absolute;left:93px;top:9px;font-size:10px;color:#fff}
.topbar .dot{position:absolute;top:6px;width:20px;height:20px;border-radius:50%;background:#fff}

.header{left:0;top:33px;width:1200px;height:82px;background:#fff}
.brandmark{position:absolute;left:94px;top:44px;font:600 15px "Montserrat",sans-serif;color:var(--ink);letter-spacing:1px;display:flex;align-items:center;gap:8px}
.brandmark i{width:14px;height:14px;background:var(--brand);display:block}
.phone{position:absolute;right:94px;top:14px;font-size:10px;color:var(--text);display:flex;gap:5px;align-items:center;white-space:nowrap}
.nav{position:absolute;top:54px;font:400 12px "Montserrat",sans-serif;color:var(--ink);white-space:nowrap}
.nav.active{color:var(--brand)}

.hero{left:0;top:115px;width:1200px;height:485px;background:linear-gradient(100deg,#8d8780 0%,#5a5856 45%,#3b3d40 100%)}
.hero .bar{position:absolute;left:750px;top:132px;width:3px;height:20px;background:var(--brand)}
.hero .kicker{position:absolute;left:769px;top:128px;font:400 17px "Montserrat",sans-serif;color:#fff;white-space:nowrap}
.hero h1{position:absolute;left:767px;top:150px;font:600 60px/60px "Montserrat",sans-serif;color:#fff;white-space:nowrap}
.hero .sub{position:absolute;left:769px;top:274px;font:400 23px "Montserrat",sans-serif;color:#fff;white-space:nowrap}
.hero .dots{position:absolute;left:1141px;top:460px;display:flex;gap:4px}
.hero .dots i{width:6px;height:6px;background:#fff;display:block}
.hero .dots i:first-child{background:var(--brand)}

.kicker-dark{font:400 18px "Montserrat",sans-serif;color:var(--ink)}
.h2{font:500 40px/44px "Montserrat",sans-serif;color:var(--ink);white-space:nowrap}
.para{font-size:13px;line-height:21px;color:var(--text)}

.section-title{position:absolute;left:0;width:1200px;text-align:center;font:500 38px "Montserrat",sans-serif;color:var(--ink)}
.focus-card{position:absolute;top:1150px;width:230px;text-align:center}
.focus-card .icon{width:94px;height:94px;margin:0 auto;border-radius:12px;background:linear-gradient(135deg,#8cbadc,#4f86b3)}
.focus-card h3{margin-top:28px;font:400 15px "Montserrat",sans-serif;color:var(--ink)}
.focus-card p{margin-top:8px;font-size:11px;line-height:17px;color:var(--muted)}
.arrow-circle{position:absolute;width:36px;height:36px;border:1px solid #cfd2d6;border-radius:50%;display:flex;align-items:center;justify-content:center}

.horizon{left:0;top:1376px;width:1200px;height:395px;background:linear-gradient(120deg,#4f88bd,#7aaad3 55%,#a7c6e3)}
.horizon-card{position:absolute;left:94px;top:1471px;width:410px;height:300px;background:#fff;padding:60px 28px 0}
.horizon-card h2{font:500 40px/42px "Montserrat",sans-serif;color:var(--ink)}
.horizon-card p{margin-top:26px;font-size:13px;line-height:21px;color:var(--text)}

.partner{position:absolute;top:1895px;width:180px;height:44px;display:flex;align-items:center;justify-content:center;gap:7px;font:600 14px "Montserrat",sans-serif;color:var(--ink);white-space:nowrap}
.partner i{width:12px;height:12px;background:var(--brand);display:block;flex:none}

.member{position:absolute;top:2123px;width:240px;text-align:center}
.member .portrait{height:244px;background:linear-gradient(180deg,#c5ccd6,#7f8996)}
.member h3{margin-top:26px;font:500 18px "Montserrat",sans-serif;color:var(--ink);letter-spacing:.3px}
.member p{margin-top:8px;font-size:12px;line-height:17px;color:var(--text);padding:0 24px}

.pillar{position:absolute;top:3005px;width:290px;text-align:center}
.pillar .icon{width:100px;height:100px;margin:0 auto;border-radius:14px;background:linear-gradient(135deg,#9fd2a3,#3d6fa8)}
.pillar h3{margin-top:30px;font:400 20px "Montserrat",sans-serif;color:var(--ink)}
.pillar p{margin-top:12px;font-size:12px;line-height:17px;color:var(--muted)}

.city{left:0;top:3290px;width:1200px;height:464px;background:linear-gradient(180deg,#2f6fc4 0%,#75a9e0 45%,#c7a77a 70%,#3d4338 100%)}
.contact-card{position:absolute;left:608px;top:3393px;width:500px;height:361px;background:#fff}
.contact-card h2{position:absolute;left:26px;top:34px;font:500 36px "Montserrat",sans-serif;color:var(--ink);white-space:nowrap}
.field{position:absolute;border:1px solid #d6d9dd;font-size:10px;color:var(--text);padding:9px 10px}
.submit{position:absolute;left:26px;top:281px;width:446px;height:38px;background:var(--brand);color:#fff;font:600 11px "Open Sans",sans-serif;display:flex;align-items:center;justify-content:center}

.footer{left:0;top:3754px;width:1200px;height:354px;background:var(--footer)}
.fcol{position:absolute;top:54px}
.fcol h4{font:600 13px "Montserrat",sans-serif;color:#fff;letter-spacing:.5px;margin-bottom:12px;white-space:nowrap}
.fcol li{list-style:none;font-size:10.5px;color:#9ea0a5;line-height:25.5px;white-space:nowrap}
.fcol p{font-size:10.5px;line-height:17.5px;color:#9ea0a5}
.social li{display:flex;align-items:center;gap:10px;line-height:29px}
.social li i{width:18px;height:18px;border-radius:50%;background:#fff;display:block}
.footbrand{position:absolute;left:93px;top:190px;font:600 14px "Montserrat",sans-serif;color:#fff;letter-spacing:1px;display:flex;align-items:center;gap:8px}
.footbrand i{width:12px;height:12px;background:#fff;display:block}
.copyright{position:absolute;left:0;top:290px;width:1200px;text-align:center;font-size:10px;color:#7a7c80}
.copyright b{color:#fff;font-weight:400}
</style>
</head>
<body>

<div class="abs topbar">
  <p>COVID-19 Response: How Brindlecrest Companies Are Taking Action.</p>
  <span class="dot" style="left:1030px"></span>
  <span class="dot" style="left:1057px"></span>
  <span class="dot" style="left:1084px"></span>
</div>

<header class="abs header">
  <div class="brandmark"><i></i>CORVANE</div>
  <div class="phone">
    <svg width="11" height="11" viewBox="0 0 24 24"><path fill="#222428" d="M6.6 10.8a15 15 0 0 0 6.6 6.6l2.2-2.2c.3-.3.7-.4 1-.2 1.1.4 2.3.6 3.6.6.6 0 1 .4 1 1V20c0 .6-.4 1-1 1A17 17 0 0 1 3 4c0-.6.4-1 1-1h3.5c.6 0 1 .4 1 1 0 1.3.2 2.5.6 3.6.1.3 0 .7-.2 1z"/></svg>
    <span>Call Us: +1 (555) 214 7730</span>
  </div>
  <span class="nav active" style="left:605px">Home</span>
  <span class="nav" style="left:680px">About Us</span>
  <span class="nav" style="left:774px">Investment Focus</span>
  <span class="nav" style="left:916px">Industry Focus</span>
  <span class="nav" style="left:1042px">Contact Us</span>
</header>

<section class="abs hero" role="img" aria-label="Photo of three business professionals standing together in an office">
  <span class="bar"></span>
  <p class="kicker">Partnering with</p>
  <h1>Exceptional<br>Leaders</h1>
  <p class="sub">Building World-Class Companies</p>
  <div class="dots"><i></i><i></i><i></i></div>
</section>
<div class="btn" style="left:769px;top:431px;width:115px;height:40px">Get Started</div>

<section class="welcome">
  <p class="abs kicker-dark" style="left:93px;top:688px">Welcome To</p>
  <h2 class="abs h2" style="left:93px;top:712px">Corvane Industries</h2>
  <p class="abs para" style="left:93px;top:766px;width:485px">Corvane Industries focuses on opportunities where it can support senior management to drive rapid growth and profit improvement through capital infusion, technology innovation and organizational expertise.&nbsp; We invest across a variety of growth industries with an emphasis on reshoring and rebuilding America.</p>
  <div class="btn" style="left:93px;top:894px;width:107px;height:33px">Read More</div>
  <div class="photo" role="img" aria-label="Photo of a presenter at a whiteboard with colleagues around a meeting table" style="left:599px;top:600px;width:601px;height:420px;background:linear-gradient(135deg,#d9dcdf,#9a9590 60%,#5f5a55)"></div>
</section>

<section class="focus">
  <h2 class="section-title" style="top:1078px">Area Of Focus</h2>
  <div class="arrow-circle" style="left:28px;top:1187px"><svg width="8" height="10" viewBox="0 0 8 10"><path d="M6 1L2 5l4 4" stroke="#333" stroke-width="1.5" fill="none"/></svg></div>
  <div class="arrow-circle" style="left:1134px;top:1187px"><svg width="8" height="10" viewBox="0 0 8 10"><path d="M2 1l4 4-4 4" stroke="#333" stroke-width="1.5" fill="none"/></svg></div>
  <div class="focus-card" style="left:105px"><div class="icon" role="img" aria-label="Illustrated shield icon"></div><h3>Defense</h3><p>Sed ut perspiciatis unde omnis iste natus error sit voluptatem...</p></div>
  <div class="focus-card" style="left:359px"><div class="icon" role="img" aria-label="Illustrated padlock and circuit icon"></div><h3>Cyber Security</h3><p>Sed ut perspiciatis unde omnis iste natus error sit voluptatem...</p></div>
  <div class="focus-card" style="left:611px"><div class="icon" role="img" aria-label="Illustrated factory buildings icon"></div><h3>Industrials</h3><p>Sed ut perspiciatis unde omnis iste natus error sit voluptatem...</p></div>
  <div class="focus-card" style="left:863px"><div class="icon" role="img" aria-label="Illustrated enterprise building with gear icon"></div><h3>Digital Enterprise</h3><p>Sed ut perspiciatis unde omnis iste natus error sit voluptatem...</p></div>
</section>

<section class="abs horizon" role="img" aria-label="Blue-toned photo of a desk with laptop, coffee cup, papers and calendar"></section>
<div class="horizon-card">
  <h2>Investment<br>Horizon</h2>
  <p>We place capital for long-term growth and revenue generation. Our investment horizon enables a focus on building strong sustainable companies, with empowered teams maximizing impact.</p>
</div>

<section class="partners">
  <svg class="abs" style="left:83px;top:1906px" width="10" height="16" viewBox="0 0 10 16"><path d="M8 2L2 8l6 6" stroke="#222" stroke-width="2" fill="none"/></svg>
  <svg class="abs" style="left:1104px;top:1906px" width="10" height="16" viewBox="0 0 10 16"><path d="M2 2l6 6-6 6" stroke="#222" stroke-width="2" fill="none"/></svg>
  <div class="partner" style="left:105px"><i></i>Pivotline PR</div>
  <div class="partner" style="left:307px">Openrange Media</div>
  <div class="partner" style="left:510px"><i></i>Ardell Capital</div>
  <div class="partner" style="left:711px"><i></i>Meridane Capital</div>
  <div class="partner" style="left:915px">Harbor Loft</div>
</section>

<section class="team">
  <h2 class="section-title" style="top:2050px">Management Team</h2>
  <div class="member" style="left:93px"><div class="portrait" role="img" aria-label="Portrait of a partner in a suit"></div><h3>WALT HENSLEY</h3><p>Walt Hensley is a Partner at Corvane Industries</p></div>
  <div class="member" style="left:351px"><div class="portrait" role="img" aria-label="Portrait of a founding partner in a suit" style="background:linear-gradient(180deg,#f2f2f2,#b9bcc0)"></div><h3>RAVI MENDHAR</h3><p>Ravi Mendhar is a Founding Partner at Corvane Industries</p></div>
  <div class="member" style="left:610px"><div class="portrait" role="img" aria-label="Portrait of a partner in a dark blazer" style="background:linear-gradient(180deg,#d7d2cb,#8d7f70)"></div><h3>NORA PETTIGREW</h3><p>Nora Pettigrew is a Partner at Corvane Industries</p></div>
  <div class="member" style="left:867px"><div class="portrait" role="img" aria-label="Portrait of a partner in a navy suit" style="background:linear-gradient(180deg,#e4e5e7,#4a5568)"></div><h3>GRANT ELLERY</h3><p>Grant Ellery is a Partner at Corvane Industries</p></div>
</section>

<section class="invest-focus">
  <div class="photo" role="img" aria-label="Photo of two colleagues reviewing documents at a table" style="left:0;top:2514px;width:600px;height:420px;background:linear-gradient(120deg,#6f6a66,#c9c3bb 55%,#e8e4de)"></div>
  <p class="abs kicker-dark" style="left:651px;top:2602px">Corvane</p>
  <h2 class="abs h2" style="left:651px;top:2626px">Investment Focus</h2>
  <p class="abs para" style="left:651px;top:2682px;width:455px">Corvane Industries partners with proven leaders, providing capital, technology innovation, and organizational expertise.&nbsp; As a holding company, we place capital for long-term growth and revenue generation. Our investment horizon enables a focus on building strong sustainable companies, with empowered teams.</p>
  <div class="btn" style="left:651px;top:2806px;width:107px;height:34px">Read More</div>
</section>

<section class="pillars">
  <div class="pillar" style="left:117px"><div class="icon" role="img" aria-label="Illustrated stack of money icon"></div><h3>Growth Capital</h3><p>Corvane Industries invests across a number of verticals, where we have specialized knowledge and relationships.</p></div>
  <div class="pillar" style="left:453px;top:2995px"><div class="icon" role="img" aria-label="Illustrated briefcase with laurel icon" style="background:linear-gradient(135deg,#f4c542,#2e5fa8)"></div><h3>Opportunistic</h3><p>We will conduct asset purchases and JV with best in class operators in specialty situations where significant opportunity...</p></div>
  <div class="pillar" style="left:792px"><div class="icon" role="img" aria-label="Illustrated city buildings with money bag icon" style="background:linear-gradient(135deg,#9fd2a3,#3b4a68)"></div><h3>Venture</h3><p>We allocate a small percentage of capital to high-potential early stage technology companies within our target...</p></div>
</section>

<section class="abs city" role="img" aria-label="Photo of a city skyline and river at golden hour"></section>
<div class="contact-card">
  <h2>Quick Contact</h2>
  <div class="field" style="left:26px;top:88px;width:220px;height:32px">Name:</div>
  <div class="field" style="left:252px;top:88px;width:220px;height:32px">Email:</div>
  <div class="field" style="left:26px;top:128px;width:220px;height:32px">Phone:</div>
  <div class="field" style="left:252px;top:128px;width:220px;height:32px">Company:</div>
  <div class="field" style="left:26px;top:166px;width:446px;height:107px">Comments:</div>
  <div class="submit">SUBMIT</div>
</div>

<footer class="abs footer">
  <div class="fcol" style="left:93px;width:280px">
    <h4>COMPANY</h4>
    <p>Corvane Industries focuses on opportunities where it can support senior management to drive rapid growth and profit improvement through capital infusion, technology innovation and organizational expertise.</p>
  </div>
  <div class="footbrand"><i></i>CORVANE</div>
  <div class="fcol" style="left:416px"><h4>QUICK LINKS</h4><ul><li>Home</li><li>About Us</li><li>Investment Focus</li><li>Industry Focus</li><li>Contact Us</li></ul></div>
  <div class="fcol" style="left:586px"><h4>QUICK LINKS</h4><ul><li>Defense &amp; Cybersecurity</li><li>Industrials &amp; Transportation</li><li>Digital Enterprise</li><li>Professional Advisory</li><li>Education</li><li>Corvane Ventures</li></ul></div>
  <div class="fcol" style="left:796px;width:190px"><h4>CONTACTS</h4><p>48 Tallow Reach, Suite 9<br>Fenwick 30217 USA</p><p style="margin-top:18px">+1 (555) 214 7730</p><p style="margin-top:24px">info@corvaneindustries.example</p></div>
  <div class="fcol social" style="left:1028px"><h4>SOCIAL ON</h4><ul><li><i></i>Chatterly</li><li><i></i>Tweetwave</li><li><i></i>Linkhall</li></ul></div>
  <p class="copyright">COPYRIGHT © 2020 <b>CORVANE INDUSTRIES</b>. ALL RIGHTS RESERVED.</p>
</footer>

</body>
</html>
```